依頼詳細
当会議が主催する講演会のチラシ製作をお願いいたします。
載せていただきたい事項は記載項目のとおりです。

【デザイン等について】
・昨年のチラシを添付しますので、参考にしてください。
・デザイン、レイアウト、色合いなどは全てお任せします
・昨年のデザインは堅苦しい印象がありましたので、今年はもう少し自由度のあるデザインを希望いたします。
・PRの強化に繋がるような、分かりやすく、且つ講演会に行きたくなる、目を引くようなデザインにしていただけたら幸いです。
・講師の写真を1枚載せてください(添付の写真データを使用願います)
・A4 縦 フルカラー
記載項目
キャッチコピー:地方の実情に合った新幹線の在り方について学ぼう

講演:「白峰新幹線実現の可能性を探る~在来線、ミニ新幹線からフル規格の新幹線へ~」

講師:鉄道ジャーナリスト 柴田 亮 氏

とき:平成28年7月5日(火) 午後3時~

ところ:桐ヶ丘グランドホテル
桐ヶ丘市松葉町二丁目3番4号

主催:北辰新幹線青葉延伸推進会議

お問い合わせ:北辰新幹線青葉延伸推進会議事務局(桐ヶ丘市役所企画課内)
Tel 0199-42-8670

※「申込不要・入場無料」の文言を入れてください。
サイズ
A4
ページ数
片面
希望イメージ
シンプル 複雑
単色 カラフル
暗い 明るい
日常 高級
遊び心 厳粛
未来的 伝統的
女性的 男性的
希望する色
納品ファイル
• イラストレーター形式 (.ai)
補足説明
※イラストレーターファイルはアウトライン必須、カラーモードはCMYKで納品願います。
※PDF形式も納品願います。
※納品は電子メール形式でお願いします。
※提案いただいたデザインの中から必ずコンペの当選者を選定します。(内容によっては修正をお願いする場合があります)
※ 募集期間を6月15日(水)としておりましたが、提案件数が希望数に達したため、誠に勝手ながら、6月14日(火)の正午をもって締め切りとさせていただく予定ですのでご了承ください。

明るく、非常に分かりやすいデザインであり、やわらかくかつポップなデザインが気に入りました。

この度は素敵なデザインを提案していただき誠にありがとうございました。
クラウドソーシングのサービスを今回初めて利用させていただきましたが、スピーディーでかつ素晴らしいデザインを提案いただき正直驚きました。想像していた以上のデザインで非常にうれしく思っております。今後ともどうか一つよろしくお願いいたします。

```html
<!DOCTYPE html>
<html lang="ja">
<head>
<meta charset="utf-8">
<title>白峰新幹線 講演会</title>
<link href="https://fonts.googleapis.com/css2?family=M+PLUS+1p:wght@500;700;800&family=Noto+Sans+JP:wght@400;500;700;900&display=swap" rel="stylesheet">
<style>
:root{
  --green:#1f7a3a;
  --green-dark:#14612c;
  --green-soft:#d9efcf;
  --green-pale:#eef8e8;
  --red:#d8232a;
  --ink:#1f2a22;
  --white:#ffffff;
}
*{margin:0;padding:0;box-sizing:border-box}
html,body{width:846px;height:1200px;overflow:hidden;background:#fff}
body{font-family:"Noto Sans JP",sans-serif;color:var(--ink)}
.flyer{position:relative;width:846px;height:1200px;overflow:hidden;background:linear-gradient(180deg,#fff 0%,#f6f8f9 45%,#fff 56%)}
.catch{position:absolute;left:18px;top:18px;background:var(--green);color:var(--white);
  font-family:"M PLUS 1p",sans-serif;font-weight:800;font-size:27px;line-height:1.45;padding:14px 22px;border-radius:10px;z-index:3}
.hero{position:absolute;left:0;top:110px;width:846px;height:470px;
  background:linear-gradient(90deg,rgba(52,128,56,.9) 0%,rgba(52,128,56,.45) 14%,rgba(52,128,56,0) 32%),
  linear-gradient(160deg,#f4f6f8 0%,#cfd8de 45%,#8fa3ad 70%,#f2f4f5 100%);
  clip-path:polygon(0 55%,60% 0,100% 8%,100% 92%,40% 100%,0 92%)}
.free{position:absolute;left:446px;top:574px;transform:rotate(-8deg);border:3px solid var(--red);background:#fff;
  color:var(--red);font-weight:900;font-size:30px;padding:4px 22px;letter-spacing:1px}
.route{position:absolute;left:262px;top:650px;display:flex;align-items:flex-end;gap:20px}
.route .stop{display:flex;flex-direction:column;align-items:flex-start}
.route .pref{font-size:23px;font-weight:700;color:var(--green-dark);margin-left:70px}
.route .station{font-size:60px;font-weight:900;color:var(--green-dark);line-height:1.05}
.route svg{margin-bottom:12px}
.lecture{position:absolute;left:0;top:770px;width:846px;height:130px;background:linear-gradient(180deg,#fff 0%,var(--green-pale) 100%)}
.lecture .tag{position:absolute;left:24px;top:18px;width:52px;height:70px;background:var(--green);color:#fff;
  font-weight:900;font-size:24px;writing-mode:vertical-rl;display:flex;align-items:center;justify-content:center;border-radius:4px}
.lecture h1{position:absolute;left:92px;top:10px;font-size:43px;font-weight:900;color:var(--green-dark);letter-spacing:1px;white-space:nowrap}
.lecture .sub{position:absolute;left:110px;top:76px;font-size:26px;font-weight:700;color:var(--green-dark);white-space:nowrap}
.details{position:absolute;left:0;top:900px;width:846px;height:215px;background:linear-gradient(180deg,var(--green-soft),#c3e3b4)}
.row{position:absolute;left:28px;display:flex;align-items:center;gap:16px}
.row .label{width:52px;height:52px;border-radius:50%;background:var(--green);color:#fff;font-size:15px;font-weight:700;
  display:flex;align-items:center;justify-content:center}
.row.when{top:18px}
.when .date{font-family:"M PLUS 1p",sans-serif;font-weight:800;color:var(--green-dark);font-size:46px}
.when .date small{font-size:26px}
.row.where{top:90px}
.where .venue{font-size:30px;font-weight:900;color:var(--green-dark);white-space:nowrap}
.where .addr{font-size:12.5px;font-weight:500;white-space:nowrap}
.row.speaker{top:154px}
.speaker .role{font-size:20px;font-weight:700}
.speaker .name{font-size:30px;font-weight:900;color:var(--green-dark);margin-left:8px}
.portrait{position:absolute;left:604px;top:900px;width:218px;height:215px;background:linear-gradient(180deg,#c9d3d7,#7a8b92)}
.footer{position:absolute;left:0;top:1115px;width:846px;height:85px;background:#fff;padding:14px 28px 0}
.footer p{font-size:17px;font-weight:500;color:var(--green-dark);line-height:1.6}
.footer p.org{padding-left:480px}
.footer .tel{font-weight:900;font-size:22px;margin-left:12px}
</style>
</head>
<body>
<div class="flyer">
  <div class="catch">地方の実情に合った<br>新幹線の在り方について学ぼう</div>
  <div class="hero" role="img" aria-label="緑の紙を破って飛び出してくる新幹線車両のイラスト"></div>
  <div class="free">申込不要・入場無料</div>

  <div class="route">
    <div class="stop"><span class="pref">北辰県</span><span class="station">白峰駅</span></div>
    <svg width="50" height="40" viewBox="0 0 50 40"><path d="M2 20H44M30 6L46 20L30 34" fill="none" stroke="#14612c" stroke-width="5"/></svg>
    <div class="stop"><span class="pref">青葉県</span><span class="station">青葉駅</span></div>
  </div>

  <section class="lecture">
    <div class="tag">講演</div>
    <h1>白峰新幹線実現の可能性を探る</h1>
    <p class="sub">～在来線、ミニ新幹線からフル規格の新幹線へ～</p>
  </section>

  <section class="details">
    <div class="row when"><span class="label">とき</span><span class="date">2016 7.5<small>(火)</small> <small>PM3:00～</small></span></div>
    <div class="row where"><span class="label">ところ</span><span class="venue">桐ヶ丘グランドホテル</span><span class="addr">桐ヶ丘市松葉町二丁目3番4号</span></div>
    <div class="row speaker"><span class="label">講師</span><span class="role">鉄道ジャーナリスト</span><span class="name">柴田 亮 氏</span></div>
  </section>
  <div class="portrait" role="img" aria-label="講師 柴田亮氏の写真"></div>

  <footer class="footer">
    <p class="org">主催／北辰新幹線青葉延伸推進会議</p>
    <p>お問い合せ／北辰新幹線青葉延伸推進会議事務局（桐ヶ丘市役所企画課内）<span class="tel">Tel 0199-42-8670</span></p>
  </footer>
</div>
</body>
</html>
```